Visitenkarten-Design für App Start Up
Zielgruppe
Wir sind ein Start-Up und haben unsere Murento App gerelauncht.
Wir haben zwei Zielgruppen für unsere App. Zum einen lokale Gewerbetreibende, welche in Echtzeit Angebote (Coupons) erstellen können und zum anderen private User, welche diese innerhalb eines vorgegebenen Zeitraumes reservieren und einlösen können.
Hierfür müssen wir auch unsere Visitenkarten auf unser neues Design anpassen.
Aufgabenstellung
Visitenkarten sollten beidseitig bedruckt sein und auf der Vorderseite sollte unser Murento Logo und/oder der App Name Murento versehen sein. Auf der Rückseite benötigen wir die Infos: Name, Position, Firma inkl. Anschrift, E-Mail sowie die Telefonnummer.
Ansonsten freuen wir uns auf weitere kreative Ansätze.

```html
<!DOCTYPE html>
<html lang="de">
<head>
<meta charset="utf-8">
<title>Murento – Visitenkarten</title>
<link rel="stylesheet" href="https://fonts.googleapis.com/css2?family=Montserrat:wght@400;500&family=Poppins:wght@400;600&display=swap">
<style>
  :root {
    --ink: #32373d;
    --text: #4a4f55;
    --magenta: #c13a82;
    --cyan: #0096cc;
    --frame: #9a9a9a;
    --paper: #ffffff;
  }
  html, body {
    margin: 0;
    width: 1200px;
    height: 903px;
    overflow: hidden;
    background: var(--paper);
  }
  .sheet { position: relative; width: 1200px; height: 903px; }
  .card {
    position: absolute;
    top: 163px;
    width: 395px;
    height: 610px;
    box-sizing: border-box;
    border: 1px solid var(--frame);
    background: var(--paper);
    font-family: "Montserrat", sans-serif;
    color: var(--text);
    text-align: center;
  }
  .card--front { left: 149px; }
  .card--back { left: 659px; }
  .card__band {
    position: absolute;
    left: -1px; right: -1px; bottom: -1px;
    height: 17px;
    background: linear-gradient(90deg, var(--magenta), var(--cyan));
  }
  .brand-square {
    position: absolute;
    left: 50%;
    top: 238px;
    width: 56px;
    height: 56px;
    margin-left: -28px;
    background: var(--magenta);
  }
  .brand-name {
    position: absolute;
    left: 0; right: 0;
    top: 366px;
    margin: 0;
    font-family: "Montserrat", sans-serif;
    font-weight: 500;
    font-size: 47px;
    letter-spacing: 7px;
    color: var(--ink);
    line-height: 1;
  }
  .brand-name--small {
    top: 122px;
    font-size: 34px;
    letter-spacing: 5px;
  }
  .person {
    position: absolute;
    left: 0; right: 0;
    top: 300px;
    font-family: "Poppins", sans-serif;
  }
  .person__name {
    margin: 0;
    font-weight: 600;
    font-size: 24px;
    line-height: 28px;
    color: var(--ink);
  }
  .person__role {
    margin: 0;
    font-weight: 400;
    font-size: 18px;
    line-height: 22px;
    color: var(--text);
  }
  .block {
    position: absolute;
    left: 0; right: 0;
    margin: 0;
    font-size: 15.5px;
    line-height: 18.5px;
  }
  .company { top: 374px; }
  .address { top: 429px; font-style: normal; }
  .contacts {
    position: absolute;
    left: 45px;
    top: 504px;
    width: 340px;
    display: grid;
    grid-template-columns: 162px 178px;
    row-gap: 20px;
    font-size: 14px;
    text-align: left;
  }
  .contact { display: flex; align-items: center; gap: 8px; height: 18px; white-space: nowrap; }
  .contact svg { width: 18px; height: 18px; flex: none; }
  .icon { fill: none; stroke: var(--cyan); stroke-width: 1.8; stroke-linecap: round; stroke-linejoin: round; }
</style>
</head>
<body>
<main class="sheet">
  <section class="card card--front" aria-label="Vorderseite">
    <div class="brand-square"></div>
    <h1 class="brand-name">MURENTO</h1>
    <div class="card__band"></div>
  </section>

  <section class="card card--back" aria-label="Rückseite">
    <p class="brand-name brand-name--small">MURENTO</p>
    <div class="person">
      <h2 class="person__name">Max Mustermann</h2>
      <p class="person__role">Geschäftsführer</p>
    </div>
    <p class="block company">Murento Entwicklungs- &amp;<br>Servicegesellschaft mbH</p>
    <address class="block address">Musterstr. 1<br>12345 Musterhausen</address>
    <div class="contacts">
      <div class="contact">
        <svg viewBox="0 0 18 18"><path class="icon" d="M3 2.5l3 0 1.3 3.2-1.8 1.4c.9 2 2.4 3.5 4.4 4.4l1.4-1.8 3.2 1.3v3c0 .6-.5 1-1 1C7.5 15 3 10.5 2 3.5c0-.5.4-1 1-1z"/></svg>
        <span>01234/ 578910</span>
      </div>
      <div class="contact">
        <svg viewBox="0 0 18 18"><path class="icon" d="M3 2.5l3 0 1.3 3.2-1.8 1.4c.9 2 2.4 3.5 4.4 4.4l1.4-1.8 3.2 1.3v3c0 .6-.5 1-1 1C7.5 15 3 10.5 2 3.5c0-.5.4-1 1-1z"/></svg>
        <span>01234/ 578910</span>
      </div>
      <div class="contact">
        <svg viewBox="0 0 18 18"><rect class="icon" x="1.5" y="3.5" width="15" height="11"/><path class="icon" d="M5.5 7.5l3.5 2.5 3.5-2.5"/></svg>
        <span>mail@murento.de</span>
      </div>
      <div class="contact">
        <svg viewBox="0 0 18 18"><circle class="icon" cx="9" cy="9" r="7.5"/><ellipse class="icon" cx="9" cy="9" rx="3" ry="7.5"/><path class="icon" d="M1.5 9h15"/></svg>
        <span>www.murento.de/info</span>
      </div>
    </div>
    <div class="card__band"></div>
  </section>
</main>
</body>
</html>
```